Make attractive Packaging label for NUT BUTTERS jars

We at Briarwood Pantry are launching our own line of NUT BUTTERS. We will be serving them in GLASS JARS ready packaged. I need attractive luxurious design for glass jar and should be designed ready to print.
I have attached glass jar pictures and measurement sheet.
My company logo has been attached. Also company details can be found on our facebook page.
product will be

ALMOND BUTTER
CASHEW BUTTER
PEANUT BUTTER
HAZELNUT BUTTER.

Industry/Entity Type

Retail

```html
<!DOCTYPE html>
<html lang="en">
<head>
<meta charset="utf-8">
<title>Briarwood Pantry – Almond Butter Jar Label</title>
<link rel="stylesheet" href="https://fonts.googleapis.com/css2?family=Lilita+One&family=Patrick+Hand+SC&family=Yellowtail&family=Open+Sans:wght@600&display=swap">
<style>
  :root {
    --page-bg: #f3f1ee;
    --label-light: #f6e9d8;
    --label-warm: #e6c9a6;
    --brown-deep: #4a2a14;
    --brown-ink: #3a2416;
    --brand-brown: #7a4520;
    --tan-band: #c99a66;
    --white: #ffffff;
    --almond-light: #d9a06a;
    --almond-dark: #8a4f25;
    --badge-red: #d9412b;
    --badge-green: #3f9a3c;
    --badge-leaf: #7cb342;
  }
  html, body {
    margin: 0;
    width: 1200px;
    height: 800px;
    overflow: hidden;
    background: var(--page-bg);
  }
  .label {
    position: absolute;
    left: 100px;
    top: 40px;
    width: 1000px;
    height: 720px;
    overflow: hidden;
    background: radial-gradient(ellipse at 50% 45%, var(--label-light) 0%, var(--label-warm) 100%);
    box-shadow: 0 6px 24px rgba(60, 35, 15, 0.18);
  }
  .swooshes {
    position: absolute;
    inset: 0;
    width: 1000px;
    height: 720px;
  }
  .tagline {
    position: absolute;
    top: 40px;
    left: 0;
    width: 100%;
    text-align: center;
    margin: 0;
    font-family: "Patrick Hand SC", cursive;
    font-size: 34px;
    letter-spacing: 3px;
    color: var(--brand-brown);
  }
  .brand-name {
    position: absolute;
    top: 120px;
    left: 0;
    width: 100%;
    margin: 0;
    text-align: center;
    font-family: "Lilita One", sans-serif;
    font-weight: 400;
    color: var(--brand-brown);
    line-height: 0.95;
  }
  .brand-name .brand-first { display: block; font-size: 118px; }
  .brand-name .brand-second { display: block; font-size: 76px; }
  .product-name {
    position: absolute;
    top: 372px;
    left: 0;
    width: 100%;
    margin: 0;
    text-align: center;
    font-family: "Yellowtail", cursive;
    font-weight: 400;
    font-size: 104px;
    color: var(--brown-ink);
  }
  .badges {
    position: absolute;
    left: 28px;
    top: 250px;
    display: flex;
    flex-direction: column;
    gap: 26px;
  }
  .badge { width: 56px; height: 56px; }
  .badge-red { background: var(--badge-red); transform: rotate(45deg) scale(0.8); border-radius: 8px; }
  .badge-green { background: var(--badge-green); border-radius: 50%; }
  .badge-leaf { background: var(--badge-leaf); border-radius: 50%; }
  .almond-art {
    position: absolute;
    right: 50px;
    bottom: 30px;
    width: 300px;
    height: 220px;
    border-radius: 46% 54% 40% 60%;
    background: radial-gradient(ellipse at 40% 40%, var(--almond-light) 0%, var(--almond-dark) 100%);
  }
  .contact {
    position: absolute;
    left: 36px;
    bottom: 44px;
    font-family: "Open Sans", sans-serif;
    font-weight: 600;
    font-size: 19px;
    color: var(--brown-ink);
    display: grid;
    grid-template-columns: auto auto;
    column-gap: 34px;
    row-gap: 10px;
  }
  .contact-item { display: flex; align-items: center; gap: 10px; }
  .contact-item.full { grid-column: 1 / 3; }
  .contact-icon { width: 20px; height: 20px; flex: none; }
</style>
</head>
<body>
  <main class="label">
    <svg class="swooshes" viewBox="0 0 1000 720" aria-hidden="true">
      <path d="M0,0 H600 C430,60 170,95 0,330 Z" fill="var(--tan-band)"/>
      <path d="M0,0 H565 C405,52 160,80 0,298 Z" fill="var(--white)"/>
      <path d="M0,0 H530 C380,40 150,62 0,272 Z" fill="var(--brown-deep)"/>
      <path d="M1000,720 H380 C590,690 850,650 1000,400 Z" fill="var(--tan-band)"/>
      <path d="M1000,720 H430 C620,700 870,665 1000,440 Z" fill="var(--white)"/>
      <path d="M1000,720 H470 C650,708 890,680 1000,470 Z" fill="var(--brown-deep)"/>
    </svg>

    <p class="tagline">Nuts • Dried Fruits • Seeds</p>

    <h1 class="brand-name">
      <span class="brand-first">Briarwood</span>
      <span class="brand-second">Pantry</span>
    </h1>

    <h2 class="product-name">Almond Butter</h2>

    <div class="badges">
      <div class="badge badge-red"></div>
      <div class="badge badge-green"></div>
      <div class="badge badge-leaf"></div>
    </div>

    <div class="almond-art" role="img" aria-label="Illustration of whole and split almonds with green leaves"></div>

    <address class="contact">
      <span class="contact-item full">
        <svg class="contact-icon" viewBox="0 0 20 20"><path d="M10 1a6 6 0 0 0-6 6c0 4.5 6 12 6 12s6-7.5 6-12a6 6 0 0 0-6-6zm0 8.5A2.5 2.5 0 1 1 10 4.5a2.5 2.5 0 0 1 0 5z" fill="var(--brown-ink)"/></svg>
        Linden Lane Market, Dublin 2.
      </span>
      <span class="contact-item">
        <svg class="contact-icon" viewBox="0 0 20 20"><circle cx="10" cy="10" r="8" fill="none" stroke="var(--brown-ink)" stroke-width="2"/><path d="M2 10h16M10 2c-3 3-3 13 0 16M10 2c3 3 3 13 0 16" fill="none" stroke="var(--brown-ink)" stroke-width="1.5"/></svg>
        www.briarwoodpantry.ie
      </span>
      <span class="contact-item">
        <svg class="contact-icon" viewBox="0 0 20 20"><path d="M5 2l3 4-2 2c1 2.5 3.5 5 6 6l2-2 4 3-2 3C9 18 2 11 2 4z" fill="var(--brown-ink)"/></svg>
        087 555 0142
      </span>
      <span class="contact-item">
        <svg class="contact-icon" viewBox="0 0 20 20"><rect x="2" y="4" width="16" height="12" rx="2" fill="none" stroke="var(--brown-ink)" stroke-width="2"/><path d="M2.5 5l7.5 6 7.5-6" fill="none" stroke="var(--brown-ink)" stroke-width="2"/></svg>
        info@briarwoodpantry.ie
      </span>
      <span class="contact-item">
        <svg class="contact-icon" viewBox="0 0 20 20"><path d="M5 2l3 4-2 2c1 2.5 3.5 5 6 6l2-2 4 3-2 3C9 18 2 11 2 4z" fill="var(--brown-ink)"/></svg>
        087 555 0187
      </span>
    </address>
  </main>
</body>
</html>
```